Business Card Design

We need a business card design for an existing business. Our main trading brand is www.brightquillsaver.co.uk

We attach various logo files - please use the version that will produce the sharpest image on the business card.

We are flexible about shape of card etc. Please think outside the box as to what goes on front and what goes on back of the card

We want to be able to amend the card (once the design has been agreed ) to add additional staff details, but the text to go on it will be generic

Details to go on card ( for the first generic one) are fairly minimal as we don't like cluttered business cards:-

Neil Cathcart
Managing Director

Mobile: 07841 258 407
Email: n.cathcart@brightquillsaver.co.uk

Industry/Entity Type

Business

```html
<!DOCTYPE html>
<html lang="en">
<head>
<meta charset="utf-8">
<title>Bright Quill Saver – Business Card</title>
<link href="https://fonts.googleapis.com/css2?family=Source+Sans+3:wght@400;600&display=swap" rel="stylesheet">
<style>
  :root {
    --backdrop: #dedede;
    --card: #ffffff;
    --brand-blue: #2a9bd6;
    --brand-light: #9fcfee;
    --navy: #1d3f5e;
    --grey: #5a5a5a;
  }
  * { margin: 0; padding: 0; box-sizing: border-box; }
  html, body {
    width: 1200px;
    height: 840px;
    overflow: hidden;
    background: var(--backdrop);
    font-family: "Source Sans 3", "Myriad Pro", Arial, sans-serif;
  }
  .canvas { position: relative; width: 1200px; height: 840px; }
  .card {
    position: absolute;
    top: 275px;
    width: 465px;
    height: 266px;
    background: var(--card);
  }
  .card--front { left: 78px; }
  .card--back { left: 654px; }

  .brand-mark {
    position: absolute;
    border-radius: 50%;
    background: var(--brand-light);
  }
  .card--front .brand-mark { left: 382px; top: 168px; width: 48px; height: 48px; }
  .card--back .brand-mark { left: 36px; top: 168px; width: 48px; height: 48px; }

  .wordmark {
    position: absolute;
    right: 78px;
    top: 214px;
    font-size: 20px;
    font-weight: 400;
    color: var(--brand-blue);
    letter-spacing: 0.1px;
  }

  .contact {
    position: absolute;
    left: 110px;
    top: 164px;
    line-height: 1;
  }
  .contact__name {
    font-size: 16px;
    font-weight: 600;
    color: var(--brand-blue);
  }
  .contact__role {
    margin-top: 4px;
    font-size: 12px;
    color: var(--navy);
  }
  .contact__phone,
  .contact__email {
    font-size: 12px;
    color: var(--grey);
  }
  .contact__phone { margin-top: 7px; }
  .contact__email { margin-top: 3px; }
</style>
</head>
<body>
  <main class="canvas">
    <section class="card card--front" aria-label="Card front">
      <span class="brand-mark" aria-hidden="true"></span>
      <p class="wordmark">brightquillsaver.co.uk</p>
    </section>

    <section class="card card--back" aria-label="Card back">
      <span class="brand-mark" aria-hidden="true"></span>
      <div class="contact">
        <p class="contact__name">Neil Cathcart</p>
        <p class="contact__role">Managing Director</p>
        <p class="contact__phone">07841 258 407</p>
        <p class="contact__email">n.cathcart@brightquillsaver.co.uk</p>
      </div>
    </section>
  </main>
</body>
</html>
```